Accommodation business card design

We need a business card designed for our long-term accommodation business based in Australia. The business card must match the style of the attached letterhead and logo. The same contact details that are on the letterhead will also go on the card except that the card must list the contact details in the following order:phone, email, home address, ABN.

The card will be printed on .76mm white pvc plastic (same as credit cards), printed both sides and will be silver foil stamped on at least one side (preferably 2 sides) The design template is attached, but please go to www.zt.com.au for more specs.

The only other addition the card will be my name: Malcolm Darby

```html
<!DOCTYPE html>
<html lang="en">
<head>
<meta charset="utf-8">
<title>Kestrel Accommodation – Business Card</title>
<link href="https://fonts.googleapis.com/css2?family=Questrial&family=Open+Sans:wght@400;600&display=swap" rel="stylesheet">
<style>
  :root {
    --maroon: #671736;
    --brown: #8a4a3c;
    --brown-text: #7d3f33;
    --white: #ffffff;
    --backdrop: #e4e4e4;
    --card-w: 540px;
    --card-h: 330px;
  }
  * { box-sizing: border-box; margin: 0; padding: 0; }
  html, body { width: 1200px; height: 900px; overflow: hidden; }
  body {
    background: var(--backdrop);
    display: flex;
    align-items: center;
    justify-content: center;
    gap: 40px;
    font-family: "Open Sans", Arial, sans-serif;
  }
  .card {
    position: relative;
    width: var(--card-w);
    height: var(--card-h);
    border-radius: 26px;
    overflow: hidden;
    box-shadow: 0 6px 18px rgba(0,0,0,0.18);
  }
  .card-shapes { position: absolute; inset: 0; width: 100%; height: 100%; }

  /* Front */
  .card-front { background: var(--white); }
  .holder { position: absolute; top: 18px; right: 30px; text-align: right; font-family: "Questrial", Arial, sans-serif; }
  .holder-name { font-size: 24px; color: var(--brown-text); line-height: 1.1; }
  .holder-role { font-size: 15px; color: var(--maroon); margin-top: 2px; }

  .brand { position: absolute; top: 80px; left: 20px; display: flex; align-items: center; gap: 18px; }
  .brand-square { width: 86px; height: 86px; background: var(--maroon); border-radius: 10px; flex: none; }
  .brand-name { font-family: "Questrial", Arial, sans-serif; color: var(--brown-text); line-height: 0.95; letter-spacing: 1px; }
  .brand-name .line-1 { display: block; font-size: 60px; }
  .brand-name .line-2 { display: block; font-size: 27px; }

  .contacts { position: absolute; left: 20px; top: 206px; list-style: none; color: var(--white); font-size: 13px; line-height: 17px; }
  .contacts li { display: flex; align-items: flex-start; gap: 7px; }
  .contacts svg { width: 11px; height: 11px; margin-top: 3px; flex: none; }
  .contacts .indent { padding-left: 18px; }
  .abn-label { color: var(--maroon); font-weight: 600; }

  /* Back */
  .card-back { background: var(--maroon); }
  .back-brand { position: absolute; right: 30px; bottom: 40px; text-align: right; font-family: "Questrial", Arial, sans-serif; color: var(--white); line-height: 0.95; letter-spacing: 1px; }
  .back-brand .line-1 { display: block; font-size: 44px; }
  .back-brand .line-2 { display: block; font-size: 19px; }
</style>
</head>
<body>

  <section class="card card-front" aria-label="Business card front">
    <svg class="card-shapes" viewBox="0 0 540 330" preserveAspectRatio="none" aria-hidden="true">
      <path d="M0,180 C160,170 330,195 540,250 L540,330 L0,330 Z" fill="var(--brown)"/>
      <path d="M110,182 C260,186 420,206 540,196 L540,226 C420,234 280,206 110,182 Z" fill="var(--maroon)"/>
    </svg>

    <div class="holder">
      <p class="holder-name">Malcolm Darby</p>
      <p class="holder-role">Manager</p>
    </div>

    <div class="brand">
      <span class="brand-square"></span>
      <p class="brand-name"><span class="line-1">KESTREL</span><span class="line-2">ACCOMMODATION</span></p>
    </div>

    <ul class="contacts">
      <li>
        <svg viewBox="0 0 12 12"><path d="M2.5 1 L4.5 1 L5.3 3.6 L4 4.6 C4.6 6 5.9 7.4 7.4 8 L8.4 6.7 L11 7.5 L11 9.5 C11 10.3 10.3 11 9.5 11 C5 11 1 7 1 2.5 C1 1.7 1.7 1 2.5 1 Z" fill="currentColor"/></svg>
        <span>0400 555 219</span>
      </li>
      <li>
        <svg viewBox="0 0 12 12"><rect x="0.5" y="2" width="11" height="8" fill="currentColor"/><path d="M0.5 2 L6 6.5 L11.5 2" stroke="var(--brown)" stroke-width="1" fill="none"/></svg>
        <span>malcolm.darby@mailbox.com</span>
      </li>
      <li>
        <svg viewBox="0 0 12 12"><path d="M6 1 L11.5 6 L10 6 L10 11 L2 11 L2 6 L0.5 6 Z" fill="currentColor"/></svg>
        <span>PO Box 1180, Harbourview Mail Centre</span>
      </li>
      <li class="indent">QLD 4700</li>
      <li class="indent"><span><span class="abn-label">ABN</span> 12 345 678 901</span></li>
    </ul>
  </section>

  <section class="card card-back" aria-label="Business card back">
    <svg class="card-shapes" viewBox="0 0 540 330" preserveAspectRatio="none" aria-hidden="true">
      <path d="M190,330 C300,230 430,175 540,150 L540,330 Z" fill="var(--brown)"/>
    </svg>
    <p class="back-brand"><span class="line-1">KESTREL</span><span class="line-2">ACCOMMODATION</span></p>
  </section>

</body>
</html>
```